Summit Path Leadership Roadmap

I've included a mock up of what I like. This design needs to be made better. I like the top section layout. It needs 5 circles for:

Please create a webpage based on this design, but improve it. Use the letterhead and business card brand you created for me to make the brand look seamless.

I love the circles - please make 5 of them the same size (can be 1 lines)

Here is the text for the circles:

Headline: Your Guided Path to Transformation
Text
Step 1: The Initial Consultation
text
Step 2: Deep-Dive Discovery and Assessment
text
Step 3: Synthesis and Strategy Formulation
text
Step 4: The Strategic Debrief Session
Text
Step 5: Implementation and Ongoing Support
Text

Also, there are many sections to this page including:

Introduction
Copy
Copy
Bio
CTA
FAQ's

Please make it interesting.

Use the colors of the mockup and my website: Corinne Valdez.com
I am including my letterhead and business card for brand coherence.

Use the fonts on my website. CorinneValdez.com

I will need all files to send to the developer. We must have ALL the art files.

Target Market(s)

see my website; CorinneValdez.com

Industry/Entity Type

See my uploads

Requirements
Must have
• all the design files

```html
<!DOCTYPE html>
<html lang="en">
<head>
<meta charset="utf-8">
<title>Summit Path Leadership — Your Guided Path</title>
<link rel="stylesheet" href="https://fonts.googleapis.com/css2?family=Playfair+Display:wght@400;500&family=Open+Sans:wght@400;600&display=swap">
<style>
:root{
  --navy:#141d45;
  --navy-deep:#0f1738;
  --gold:#a4814e;
  --gold-light:#e2bf78;
  --teal:#2f88a7;
  --grey-text:#6d6d72;
  --faq-bg:#f1f1f1;
  --white:#ffffff;
}
*{box-sizing:border-box;margin:0;padding:0}
html,body{width:1200px;height:3602px;overflow:hidden;background:var(--white)}
body{position:relative;font-family:"Open Sans",Arial,sans-serif;color:var(--navy)}
.abs{position:absolute}
.heading{font-family:"Playfair Display",Georgia,serif;font-weight:400;text-transform:uppercase;letter-spacing:.3px}
.rule{position:absolute;height:2px;background:var(--gold)}

/* brand */
.brand{display:flex;flex-direction:column;align-items:center;color:var(--white)}
.brand-mark{width:46px;height:46px;border-radius:50%;background:var(--gold)}
.brand-name{font-family:"Open Sans",Arial,sans-serif;font-weight:600;font-size:16px;margin-top:14px;white-space:nowrap;color:var(--white)}

/* hero */
.hero-panel{left:0;top:0;width:645px;height:677px;background:var(--navy)}
.hero-photo{left:645px;top:0;width:555px;height:677px;background:linear-gradient(160deg,#c9c4bc 0%,#8e8a86 45%,#1c2447 100%)}
.hero-title{left:75px;top:232px;font-size:48px;line-height:57px;color:var(--white)}
.hero-text{left:75px;top:433px;width:470px;font-size:13px;line-height:19px;color:var(--white)}

/* steps */
.step{width:196px;height:204px;top:766px}
.step-ring{position:absolute;left:0;top:0;width:196px;height:196px;border-radius:50%;background:linear-gradient(150deg,#d9b878,#8a6a3b 55%,#e0c186)}
.step-core{position:absolute;left:6px;top:6px;width:184px;height:184px;border-radius:50%;background:var(--navy);display:flex;flex-direction:column;align-items:center}
.step-num{width:58px;height:58px;border-radius:50%;background:var(--teal);margin-top:23px;display:flex;align-items:center;justify-content:center;font-family:"Playfair Display",Georgia,serif;font-size:30px;color:var(--white)}
.step-num.is-gold{background:linear-gradient(150deg,var(--gold-light),var(--gold))}
.step-label{margin-top:14px;font-family:"Playfair Display",Georgia,serif;font-size:14px;line-height:19px;text-transform:uppercase;color:var(--white);text-align:center}
.step-tip{position:absolute;left:86px;top:190px;width:0;height:0;border-left:12px solid transparent;border-right:12px solid transparent;border-top:12px solid var(--navy)}

/* intro */
.intro-photo{left:175px;top:1053px;width:436px;height:351px;background:linear-gradient(180deg,#6f93b7 0%,#c99aa4 40%,#e8b88b 55%,#3b5068 100%)}
.section-title{font-size:38px;line-height:44px;color:var(--navy)}
.body-grey{font-size:12px;line-height:19px;color:var(--grey-text)}

/* power band */
.power-band{left:0;top:1510px;width:1200px;height:430px;background:var(--gold)}
.power-photo{left:611px;top:1510px;width:513px;height:430px;background:linear-gradient(160deg,#f2c274 0%,#7d8a3f 40%,#cfd4d4 60%,#3f4f2a 100%)}
.power-title{left:75px;top:1596px;font-size:38px;line-height:42px;color:var(--white)}
.power-text{left:75px;top:1707px;width:450px;font-size:12px;line-height:19px;color:var(--white)}
.arrow-btn{width:40px;height:40px;border-radius:50%;top:1805px;display:flex;align-items:center;justify-content:center}
.arrow-btn.prev{left:75px;background:var(--white)}
.arrow-btn.next{left:120px;background:var(--navy)}

/* about */
.about-photo{left:150px;top:2038px;width:437px;height:351px;background:linear-gradient(180deg,#e6e6e6 0%,#e2dedb 55%,#1f3f36 100%)}

/* cta */
.cta{left:77px;top:2488px;width:1047px;height:221px;background:var(--teal)}
.cta-title{left:0;top:34px;width:1047px;text-align:center;font-size:38px;line-height:44px;color:var(--white)}
.cta-text{left:0;top:106px;width:1047px;text-align:center;font-size:12.5px;color:var(--white)}
.cta-button{left:410px;top:143px;width:227px;height:36px;background:linear-gradient(90deg,#b28b4f,var(--gold-light));color:var(--white);font-size:12.5px;font-weight:600;display:flex;align-items:center;justify-content:center}

/* faq */
.faq-title{left:0;top:2798px;width:1200px;text-align:center;font-size:38px;line-height:46px;color:var(--navy)}
.faq-item{left:232px;width:736px;background:var(--faq-bg)}
.faq-q{position:absolute;left:21px;font-family:"Playfair Display",Georgia,serif;font-variant-numeric:lining-nums;font-size:14px;text-transform:uppercase;color:var(--navy)}
.faq-a{position:absolute;left:21px;width:460px;font-size:12px;line-height:19px;color:var(--grey-text)}
.faq-toggle{position:absolute;right:25px;width:19px;height:19px;border-radius:50%;background:var(--navy);display:flex;align-items:center;justify-content:center}

/* footer */
.footer{left:0;top:3287px;width:1200px;height:315px;background:var(--navy)}
.footer-divider{position:absolute;width:1px;background:rgba(255,255,255,.25)}
.contact{left:380px;top:69px;font-size:12.5px;line-height:19px;color:var(--white)}
.contact-row{display:flex;align-items:center;gap:10px}
.contact-row svg{flex:none}
.news-title{left:708px;top:62px;font-family:"Playfair Display",Georgia,serif;font-size:23px;color:var(--white)}
.news-text{left:709px;top:108px;width:400px;font-size:12.5px;line-height:17px;color:var(--white)}
.news-input{left:709px;top:148px;width:393px;height:36px;background:var(--white);font-size:12px;color:#555;display:flex;align-items:center;padding-left:19px}
.footer-rule{left:75px;top:258px;width:1050px;height:1px;background:rgba(255,255,255,.25)}
.copyright{left:0;top:271px;width:1200px;text-align:center;font-size:11px;line-height:15px;color:var(--white)}
</style>
</head>
<body>

<!-- hero -->
<section class="abs hero-panel">
  <div class="abs brand" style="left:75px;top:16px;width:172px">
    <div class="brand-mark"></div>
    <div class="brand-name">Summit Path Leadership</div>
  </div>
  <h1 class="abs heading hero-title">Welcome to<br>your guided path<br>to transformation</h1>
  <div class="rule" style="left:75px;top:413px;width:136px"></div>
  <p class="abs hero-text">Discover a proven, transformative process designed to unlock your potential, align your purpose, and bring meaningful results to your professional and personal life.</p>
</section>
<div class="abs hero-photo" role="img" aria-label="Portrait of the coach in a navy suit, arms crossed, in a bright office"></div>

<!-- steps -->
<div class="abs step" style="left:74px"><div class="step-ring"></div><div class="step-core"><div class="step-num">01</div><div class="step-label">The Initial<br>Consultation</div></div><div class="step-tip"></div></div>
<div class="abs step" style="left:288px"><div class="step-ring"></div><div class="step-core"><div class="step-num">02</div><div class="step-label">Deep - Dive<br>Discovery</div></div><div class="step-tip"></div></div>
<div class="abs step" style="left:501px"><div class="step-ring"></div><div class="step-core"><div class="step-num is-gold">03</div><div class="step-label">Strategy<br>Formulation</div></div><div class="step-tip"></div></div>
<div class="abs step" style="left:715px"><div class="step-ring"></div><div class="step-core"><div class="step-num">04</div><div class="step-label">The Strategic<br>Debrief Session</div></div><div class="step-tip"></div></div>
<div class="abs step" style="left:929px"><div class="step-ring"></div><div class="step-core"><div class="step-num">05</div><div class="step-label">Implementation &amp;<br>Ongoing Support</div></div><div class="step-tip"></div></div>

<!-- introduction -->
<div class="abs intro-photo" role="img" aria-label="Calm sea at sunset under pink clouds"></div>
<h2 class="abs heading section-title" style="left:657px;top:1134px">Introduction</h2>
<div class="rule" style="left:657px;top:1184px;width:136px"></div>
<p class="abs body-grey" style="left:657px;top:1204px;width:380px">Transformation doesn't happen by chance—it happens by design. At Corinne Valdez Consulting, we guide leaders, professionals, and visionaries through a process of genuine growth and purposeful alignment. Whether you seek clarity, leadership development, or organizational change, this pathway provides the framework for lasting success.</p>

<!-- power of a guided process -->
<section class="abs power-band"></section>
<div class="abs power-photo" role="img" aria-label="Waterfall in a sunlit forest gorge"></div>
<h2 class="abs heading power-title">The power<br>of a guided process</h2>
<div class="rule" style="left:75px;top:1689px;width:136px;background:var(--white)"></div>
<p class="abs power-text">Our process is built on decades of experience helping individuals and organizations create meaningful change. By blending neuroscience, leadership psychology, and transformational coaching, we help you move from insight to implementation with clarity and confidence.</p>
<div class="abs arrow-btn prev"><svg width="10" height="10" viewBox="0 0 10 10"><path d="M6.5 2 L3.5 5 L6.5 8" fill="none" stroke="#141d45" stroke-width="1.6"/></svg></div>
<div class="abs arrow-btn next"><svg width="10" height="10" viewBox="0 0 10 10"><path d="M3.5 2 L6.5 5 L3.5 8" fill="none" stroke="#ffffff" stroke-width="1.6"/></svg></div>

<!-- about -->
<div class="abs about-photo" role="img" aria-label="Portrait of the coach in a dark green blazer on a light grey backdrop"></div>
<h2 class="abs heading section-title" style="left:632px;top:2112px">About us</h2>
<div class="rule" style="left:632px;top:2161px;width:108px"></div>
<p class="abs body-grey" style="left:632px;top:2183px;width:420px">Corinne Valdez is an award-winning author, leadership expert, and transformation coach with over 25 years of experience guiding individuals and organizations toward their highest potential.</p>
<p class="abs body-grey" style="left:632px;top:2252px;width:420px">Her work is grounded in science, elevated by intuition, and inspired by the human spirit. Corinne's clients include executives, entrepreneurs, and change-makers committed to living and leading with purpose.</p>

<!-- call to action -->
<section class="abs cta">
  <h2 class="abs heading cta-title">Start your transformation today</h2>
  <div class="rule" style="left:456px;top:90px;width:135px;background:var(--white)"></div>
  <p class="abs cta-text">Schedule your private consultation to begin your personalized journey.</p>
  <div class="abs cta-button">Schedule My Consultation</div>
</section>

<!-- faq -->
<h2 class="abs heading faq-title">Frequently asked questions</h2>
<div class="rule" style="left:545px;top:2851px;width:112px"></div>

<div class="abs faq-item" style="top:2882px;height:105px">
  <div class="faq-q" style="top:20px">Q1: What can I expect during the first consultation?</div>
  <div class="faq-toggle" style="top:22px"><svg width="8" height="8" viewBox="0 0 8 8"><path d="M1.5 3 L4 5.5 L6.5 3" fill="none" stroke="#fff" stroke-width="1.3"/></svg></div>
  <p class="faq-a" style="top:46px">A welcoming, confidential conversation focused on your goals, challenges, and desired outcomes.</p>
</div>
<div class="abs faq-item" style="top:2996px;height:41px"><div class="faq-q" style="top:11px">Q2: How long does the full process take?</div><div class="faq-toggle" style="top:11px"><svg width="8" height="8" viewBox="0 0 8 8"><path d="M1.5 5 L4 2.5 L6.5 5" fill="none" stroke="#fff" stroke-width="1.3"/></svg></div></div>
<div class="abs faq-item" style="top:3047px;height:41px"><div class="faq-q" style="top:11px">Q3: Is this process suitable for organizations?</div><div class="faq-toggle" style="top:11px"><svg width="8" height="8" viewBox="0 0 8 8"><path d="M1.5 5 L4 2.5 L6.5 5" fill="none" stroke="#fff" stroke-width="1.3"/></svg></div></div>
<div class="abs faq-item" style="top:3098px;height:41px"><div class="faq-q" style="top:11px">Q4: What's the investment?</div><div class="faq-toggle" style="top:11px"><svg width="8" height="8" viewBox="0 0 8 8"><path d="M1.5 5 L4 2.5 L6.5 5" fill="none" stroke="#fff" stroke-width="1.3"/></svg></div></div>
<div class="abs faq-item" style="top:3148px;height:41px"><div class="faq-q" style="top:11px">Q5: How do I get started?</div><div class="faq-toggle" style="top:11px"><svg width="8" height="8" viewBox="0 0 8 8"><path d="M1.5 5 L4 2.5 L6.5 5" fill="none" stroke="#fff" stroke-width="1.3"/></svg></div></div>

<!-- footer -->
<footer class="abs footer">
  <div class="abs brand" style="left:85px;top:62px;width:216px">
    <div class="brand-mark" style="width:64px;height:64px"></div>
    <div class="brand-name" style="font-size:19px;margin-top:22px">Summit Path Leadership</div>
  </div>
  <div class="footer-divider" style="left:358px;top:58px;height:140px"></div>
  <div class="abs contact">
    <div>418 Harbor Lane,</div>
    <div>Ste 210</div>
    <div>Portland, Oregon 97205-1180</div>
    <div class="contact-row"><svg width="12" height="12" viewBox="0 0 12 12"><path d="M3 1 L5 3.5 L4 5 Q5.5 7.5 7 8 L8.5 7 L11 9 L9.5 11 Q4 10.5 1 3 Z" fill="#a4814e"/></svg>555-318-2047</div>
    <div class="contact-row"><svg width="12" height="12" viewBox="0 0 12 12"><rect x="1" y="2.5" width="10" height="7" fill="#a4814e"/><path d="M1 2.5 L6 6.5 L11 2.5" fill="none" stroke="#141d45" stroke-width="1"/></svg>corinne@corinnevaldez.com</div>
    <div class="contact-row"><svg width="12" height="12" viewBox="0 0 12 12"><circle cx="6" cy="6" r="5" fill="#a4814e"/><path d="M1 6 H11 M6 1 Q3 6 6 11 Q9 6 6 1" fill="none" stroke="#141d45" stroke-width=".8"/></svg>www.corinnevaldez.com</div>
  </div>
  <div class="footer-divider" style="left:677px;top:58px;height:140px"></div>
  <div class="abs news-title">Newsletter</div>
  <p class="abs news-text">Subscribe to our newsletter to receive updates on new product offerings...</p>
  <div class="abs news-input">Enter email
    <svg style="position:absolute;right:16px;top:12px" width="13" height="13" viewBox="0 0 13 13"><path d="M1 6 L12 1 L8 12 L6 7 Z" fill="#a4814e"/></svg>
  </div>
  <div class="abs footer-rule"></div>
  <p class="abs copyright">Summit Path Leadership is a premier suite of consulting services by Corinne Valdez International.<br>© All rights reserved</p>
</footer>

</body>
</html>
```